Business Card - Professional Minimalist - Double sided

We appreciate minimalist logo/web/collateral designs that allow design to tell a story. We want to relay a professional image/approach but throwing in a splash of modern when we’re able so long as it’s not distracting. Think 75% classic corporate, 25% modern. Open to black or white design, not sure which might look the best.

Target Market(s)

Senior executives or related government affairs contacts within the agriculture, energy, and defense industries (i.e., potential clients) but located outside of Washington, DC. Most potential clients based in DC with be familiar with both of us and our shared history.

Industry/Entity Type

Consulting

Contact Information for Business Card

Name: Daniel R. Whitlock
Title: Co-Founder & Partner
Address: 418 Bramblewood Ave. SE | Suite 2716 | Washington, D.C. 20019
Phone: (202) 555-0187
Email: Daniel@HollerbyWhitlock.com

Font styles to use
Serif

Colors

Designer to choose only greyscale colors for use in the design.

Requirements
Must have
• Name: Daniel R. Whitlock
Phone: (202) 555-0187

```html
<!DOCTYPE html>
<html lang="en">
<head>
<meta charset="utf-8">
<title>Hollerby Whitlock Group — Business Card</title>
<link rel="stylesheet" href="https://fonts.googleapis.com/css2?family=Libre+Baskerville:wght@400;700&family=Source+Serif+4:wght@400&display=swap">
<style>
  :root {
    --page: #ffffff;
    --card: #040404;
    --card-edge: #2e2e2e;
    --motif: #141414;
    --brand: #8c8c8c;
    --name: #9d9d9d;
    --text: #b4b4b4;
  }
  * { margin: 0; padding: 0; box-sizing: border-box; }
  html, body {
    width: 1084px; height: 1200px; overflow: hidden;
    background: var(--page);
  }
  .canvas { position: relative; width: 1084px; height: 1200px; }
  .card {
    position: absolute; width: 486px; height: 314px;
    background: var(--card);
    border: 1px solid var(--card-edge);
    overflow: hidden;
  }
  .card--front { left: 203px; top: 251px; }
  .card--back  { left: 367px; top: 593px; }

  .motif {
    position: absolute; top: 2px; bottom: 0; width: 156px;
    background: linear-gradient(180deg, #171717, var(--motif));
  }
  .card--front .motif { right: 0; }
  .card--back .motif  { left: 0; }

  .brand {
    position: absolute; left: 32px; top: 36px;
    display: flex; align-items: center; gap: 9px;
  }
  .brand__mark { width: 30px; height: 30px; background: var(--brand); }
  .brand__name {
    font-family: "Libre Baskerville", serif; font-weight: 400;
    font-size: 13px; letter-spacing: 1.2px; text-transform: uppercase;
    color: var(--brand);
  }

  .person { position: absolute; left: 35px; top: 232px; }
  .person__name {
    font-family: "Libre Baskerville", serif; font-weight: 700;
    font-size: 16px; color: var(--name); letter-spacing: 0.3px;
  }
  .person__title {
    font-family: "Libre Baskerville", serif; font-weight: 400;
    font-size: 12.5px; color: var(--text); margin-top: 3px;
  }

  .contact {
    position: absolute; left: 262px; top: 236px;
    font-family: "Source Serif 4", serif; font-size: 12px;
    line-height: 14.5px; color: var(--text); list-style: none;
  }
  .contact__phone { margin-bottom: 2px; }
</style>
</head>
<body>
  <main class="canvas">
    <section class="card card--front" aria-label="Card front">
      <div class="brand">
        <span class="brand__mark" aria-hidden="true"></span>
        <span class="brand__name">Hollerby Whitlock Group</span>
      </div>
      <div class="motif" role="img" aria-label="Large faint brand motif"></div>
    </section>

    <section class="card card--back" aria-label="Card back">
      <div class="motif" role="img" aria-label="Large faint brand motif"></div>
      <div class="person">
        <p class="person__name">Daniel R. Whitlock</p>
        <p class="person__title">Co-Founder &amp; Partner</p>
      </div>
      <ul class="contact">
        <li class="contact__phone">(202) 555-0187</li>
        <li>Daniel@HollerbyWhitlock.com</li>
        <li>418 Bramblewood Ave. SE</li>
        <li>Suite 2716 | Washington, D.C. 20019</li>
      </ul>
    </section>
  </main>
</body>
</html>
```